Velvet Pressings Techno Label Business Card

I'm looking for a very clean business card for my Velvet Pressings music label. The label focusses on techno music. The card should include:

• my name : Bram Quintel as "Founder & CEO"
• email address: bram@velvet-pressings.example
• web: www.velvet-pressings.example
• /velvetpress logo + /velvetpress
• /velvetpress logo + /velvetpress
• soundcloud logo + /velvetpressings

Feel free to include your ideas! I'm looking forward to discuss about it.

Bram

Industry/Entity Type

Business

Contact Information for Business Card

I don't like glossy cards. Prefer matt.

Requirements
Nice to have
• Maybe on one side the complete logo, other side just the icon.
Should not have
• Flashy stuff. Must be clean and business like style.

```html
<!DOCTYPE html>
<html lang="en">
<head>
<meta charset="utf-8">
<title>Velvet Pressings — Business Card</title>
<link rel="stylesheet" href="https://fonts.googleapis.com/css2?family=Montserrat:wght@400;500;600&family=Oswald:wght@400;500&display=swap">
<style>
  :root {
    --orange: #f26a1b;
    --ink: #4a4a4a;
    --ink-soft: #6b6b6b;
    --rule: #5a5a5a;
    --card: #ffffff;
    --stage-top: #e4e4e4;
    --stage-bottom: #c9c9c9;
  }
  * { box-sizing: border-box; margin: 0; padding: 0; }
  html, body { width: 1200px; height: 947px; overflow: hidden; }
  body {
    background: linear-gradient(180deg, var(--stage-top), var(--stage-bottom));
    font-family: "Montserrat", sans-serif;
    color: var(--ink);
    display: flex;
    align-items: center;
    justify-content: center;
    gap: 90px;
  }
  .card {
    width: 400px;
    height: 660px;
    background: var(--card);
    border-radius: 22px;
    box-shadow: 0 18px 40px rgba(0,0,0,0.18);
    position: relative;
  }

  /* Front */
  .card--front { padding: 70px 40px 0 56px; }
  .brand {
    display: flex;
    align-items: center;
    gap: 14px;
    margin-bottom: 78px;
  }
  .brand__dot {
    width: 30px; height: 30px;
    border-radius: 50%;
    background: var(--orange);
    flex: none;
  }
  .brand__name {
    font-family: "Montserrat", sans-serif;
    font-weight: 600;
    font-size: 27px;
    color: var(--orange);
    letter-spacing: 0.2px;
    white-space: nowrap;
  }
  .contact-row {
    display: flex;
    align-items: center;
    gap: 16px;
    margin-bottom: 62px;
  }
  .contact-row__icon { width: 38px; height: 38px; flex: none; }
  .contact-row__icon svg { width: 100%; height: 100%; display: block; }
  .contact-row__rule {
    width: 4px;
    align-self: stretch;
    background: var(--rule);
    flex: none;
  }
  .contact-row__text {
    font-size: 14px;
    line-height: 1.4;
    letter-spacing: 0.4px;
    color: var(--ink);
    white-space: nowrap;
  }
  .person__name {
    font-family: "Oswald", sans-serif;
    font-weight: 400;
    font-size: 25px;
    letter-spacing: 1.5px;
    color: var(--orange);
    text-transform: uppercase;
    line-height: 1.1;
  }
  .person__role {
    font-size: 13px;
    letter-spacing: 0.8px;
    color: var(--ink-soft);
  }

  /* Back */
  .card--back {
    display: flex;
    align-items: center;
    justify-content: center;
  }
  .brand--center { margin: 0; flex-direction: column; gap: 18px; }
  .brand--center .brand__dot { width: 74px; height: 74px; }
  .brand--center .brand__name { font-size: 25px; }
  .social {
    position: absolute;
    right: 28px;
    bottom: 32px;
    display: flex;
    gap: 14px;
  }
  .social__item {
    display: flex;
    align-items: center;
    gap: 6px;
    font-size: 11px;
    letter-spacing: 0.3px;
    color: var(--ink-soft);
    white-space: nowrap;
  }
  .social__mark {
    width: 14px; height: 14px;
    background: var(--orange);
    border-radius: 2px;
    flex: none;
  }
</style>
</head>
<body>

  <section class="card card--front" aria-label="Card front">
    <div class="brand">
      <span class="brand__dot"></span>
      <span class="brand__name">Velvet Pressings</span>
    </div>

    <div class="contact-row">
      <span class="contact-row__icon">
        <svg viewBox="0 0 40 40" aria-hidden="true">
          <circle cx="20" cy="12" r="8" fill="var(--orange)"/>
          <path d="M4 38c0-10 7-16 16-16s16 6 16 16z" fill="var(--orange)"/>
        </svg>
      </span>
      <span class="contact-row__rule"></span>
      <div class="contact-row__text">
        <div class="person__name">Bram Quintel</div>
        <div class="person__role">Founder &amp; CEO</div>
      </div>
    </div>

    <div class="contact-row">
      <span class="contact-row__icon">
        <svg viewBox="0 0 40 40" aria-hidden="true">
          <path d="M20 2c-8 0-14 6-14 14 0 10 14 22 14 22s14-12 14-22c0-8-6-14-14-14z" fill="var(--orange)"/>
          <circle cx="20" cy="16" r="5" fill="#fff"/>
        </svg>
      </span>
      <span class="contact-row__rule"></span>
      <div class="contact-row__text">
        417 9th floor Arcade<br>Marlow Lane KTR
      </div>
    </div>

    <div class="contact-row">
      <span class="contact-row__icon">
        <svg viewBox="0 0 40 40" aria-hidden="true">
          <circle cx="20" cy="20" r="17" fill="var(--orange)"/>
          <g fill="none" stroke="#fff" stroke-width="2">
            <ellipse cx="20" cy="20" rx="7" ry="17"/>
            <line x1="3" y1="20" x2="37" y2="20"/>
            <line x1="20" y1="3" x2="20" y2="37"/>
            <path d="M6 11h28M6 29h28"/>
          </g>
        </svg>
      </span>
      <span class="contact-row__rule"></span>
      <div class="contact-row__text">
        014 582 3907<br>bram@velvet-pressings.example<br>www.velvet-pressings.example
      </div>
    </div>
  </section>

  <section class="card card--back" aria-label="Card back">
    <div class="brand brand--center">
      <span class="brand__dot"></span>
      <span class="brand__name">Velvet Pressings</span>
    </div>
    <div class="social">
      <span class="social__item"><span class="social__mark"></span>/velvetpress</span>
      <span class="social__item"><span class="social__mark"></span>/velvetpress</span>
      <span class="social__item"><span class="social__mark"></span>/velvetpressings</span>
    </div>
  </section>

</body>
</html>
```